Welcome Package Cover

We want to design a new cover for our welcome package. The dimensions are 4 1/4" x 9". We are a church in London Ontario called BRAVELY Church. Our website is www.bravelyonward.ca
We don't want it to be churchy or religious looking. We want it to be fresh and youthful.
Can use backgrounds unique to London Ontario Canada
I will attach our logo designs.

```html
<!DOCTYPE html>
<html lang="en">
<head>
<meta charset="utf-8">
<title>BRAVELY Church – Welcome Package Cover</title>
<link href="https://fonts.googleapis.com/css2?family=Tinos:wght@400;700&display=swap" rel="stylesheet">
<style>
  :root {
    --backdrop: #e6e0f0;
    --paper: #ffffff;
    --navy: #1c1f5a;
    --gold: #a9823f;
    --violet-light: #d9c8ee;
    --violet: #9a6cc8;
    --violet-deep: #6a3fa0;
    --corner: #2c2f86;
    --sky-top: #3b3f9e;
    --sky-mid: #8a7bc9;
    --sky-glow: #e2a6d6;
    --river: #2a2f7a;
  }
  * { box-sizing: border-box; margin: 0; padding: 0; }
  html, body {
    width: 1200px; height: 1200px; overflow: hidden;
    background: var(--backdrop);
  }
  .stage {
    width: 1200px; height: 1200px;
    display: flex; align-items: center; justify-content: center;
  }
  .cover {
    position: relative;
    width: 472px; height: 1000px;
    background: var(--paper);
    box-shadow: 0 12px 30px rgba(40, 20, 80, 0.25);
    overflow: hidden;
  }
  .cover-art { position: absolute; inset: 0; width: 100%; height: 100%; }
  .brand {
    position: absolute; left: 26px; top: 48px;
    width: 230px;
  }
  .brand-name {
    font-family: "Tinos", serif;
    font-weight: 700;
    font-size: 30px; line-height: 1.1;
    color: var(--navy);
  }
  .tagline {
    margin-top: 8px;
    font-family: "Tinos", serif;
    font-weight: 400;
    font-size: 11px; line-height: 1.25;
    color: var(--gold);
  }
</style>
</head>
<body>
<main class="stage">
  <section class="cover">
    <svg class="cover-art" viewBox="0 0 472 1000" preserveAspectRatio="none">
      <defs>
        <linearGradient id="photo-tones" x1="0" y1="0" x2="0" y2="1">
          <stop offset="0" stop-color="var(--sky-top)"/>
          <stop offset="0.45" stop-color="var(--sky-mid)"/>
          <stop offset="0.62" stop-color="var(--sky-glow)"/>
          <stop offset="0.72" stop-color="var(--violet-deep)"/>
          <stop offset="1" stop-color="var(--river)"/>
        </linearGradient>
        <linearGradient id="band-tones" x1="0" y1="1" x2="1" y2="0">
          <stop offset="0" stop-color="var(--violet-deep)"/>
          <stop offset="0.5" stop-color="var(--violet-light)"/>
          <stop offset="1" stop-color="var(--violet)"/>
        </linearGradient>
      </defs>
      <path class="photo-window" role="img"
            aria-label="Photo of a lit city bridge over a river at dusk, purple sky and reflections on the water"
            d="M0,1000 L0,790 C40,500 180,250 340,120 C400,150 445,190 472,235 L472,1000 Z"
            fill="url(#photo-tones)"/>
      <path class="arc-band rising" d="M-10,800 C30,470 190,210 490,-20"
            fill="none" stroke="url(#band-tones)" stroke-width="44"/>
      <path class="arc-band falling" d="M270,-30 C360,20 440,110 500,260"
            fill="none" stroke="url(#band-tones)" stroke-width="40"/>
      <path class="corner-tab" d="M395,0 L472,0 L472,75 Z" fill="var(--corner)"/>
    </svg>
    <header class="brand">
      <h1 class="brand-name">BRAVELY Church</h1>
      <p class="tagline">Growing Together to<br>Serve Our City Well</p>
    </header>
  </section>
</main>
</body>
</html>
```